The Yarrawin Pet Groomer

I have a logo which I designed myself ( I tried a contest and it did not work out well..not on this site) The logo needs some tweaking for example "THE" needs to be put above "YARRAWIN" in line with the D (on top)and it needs to be going across sideways.Also the dog is not exactly in the middle.
Also on the card I would like my name written in a simple running writing script
Marnie

Then in plain writing:
27B Fenwick St Mudgee NSW 2850
Ph. 6319 5057
On the back:
Your next appointment:
...........................................

Pet bathing, clipping and styling

Pet

Must have
• The logo going across lengthways and changed a bit (as explained above)

```html
<!DOCTYPE html>
<html lang="en">
<head>
<meta charset="utf-8">
<title>The Yarrawin Pet Groomer – Business Card</title>
<link href="https://fonts.googleapis.com/css2?family=Tinos:wght@400;700&family=Pinyon+Script&display=swap" rel="stylesheet">
<style>
  :root {
    --page: #ffffff;
    --card: #fde6f8;
    --band: #f9c3df;
    --strip: #f7b9dc;
    --strip-inner: #fbd9ec;
    --paw-red: #e8202a;
    --art-light: #eef2f6;
    --art-dark: #c7ced8;
    --ink: #111111;
    --brand: #1f1f1f;
  }
  * { box-sizing: border-box; margin: 0; padding: 0; }
  html, body {
    width: 904px; height: 1200px; overflow: hidden;
    background: var(--page);
  }
  .sheet { position: relative; width: 904px; height: 1200px; font-family: "Tinos", serif; color: var(--ink); }
  .side-label {
    position: absolute; left: 0; width: 904px; text-align: center;
    font-size: 38px; line-height: 1;
  }
  .side-label.front { top: 22px; }
  .side-label.back { top: 582px; }

  .card { position: absolute; left: 107px; width: 690px; height: 444px; background: var(--card); overflow: hidden; }
  .card.front { top: 93px; }
  .card.back { top: 658px; }

  .paw-strip {
    position: absolute; left: 0; top: 0; width: 176px; height: 100%;
    background: linear-gradient(90deg, var(--strip) 0 12%, var(--strip-inner) 12% 88%, var(--strip) 88% 100%);
  }
  .brand-name {
    position: absolute; left: 250px; top: 130px; width: 400px;
    font-family: "Tinos", serif; font-weight: 700; font-size: 64px; line-height: 1.05;
    color: var(--brand); text-align: center; letter-spacing: 1px;
  }
  .owner-name {
    position: absolute; left: 330px; top: 360px; width: 330px; text-align: center;
    font-family: "Pinyon Script", cursive; font-size: 64px; line-height: 1; color: var(--ink);
  }

  .services {
    position: absolute; top: 24px; left: 0; width: 100%; text-align: center;
    font-size: 27px;
  }
  .appointment-band {
    position: absolute; left: 0; top: 147px; width: 515px; height: 155px; background: var(--band);
  }
  .appointment-label {
    position: absolute; left: 48px; top: 38px; font-size: 40px; line-height: 1;
  }
  .appointment-line {
    position: absolute; left: 48px; top: 121px; width: 396px; height: 2px; background: var(--ink);
  }
  .mascot-art {
    position: absolute; left: 500px; top: 90px; width: 186px; height: 228px;
    border-radius: 45% 45% 40% 40%;
    background: radial-gradient(circle at 50% 45%, var(--art-light) 0 55%, var(--art-dark) 100%);
  }
  .contact {
    position: absolute; left: 0; bottom: 20px; width: 100%; text-align: center; font-size: 27px;
  }
</style>
</head>
<body>
<main class="sheet">
  <p class="side-label front">side 1</p>
  <section class="card front">
    <div class="paw-strip" role="img" aria-label="Decorative band of red and white paw prints on pink"></div>
    <h1 class="brand-name">The Yarrawin<br>Pet Groomer</h1>
    <p class="owner-name">Marnie</p>
  </section>

  <p class="side-label back">side 2</p>
  <section class="card back">
    <p class="services">Pet Bathing, Clipping and Styling</p>
    <div class="appointment-band">
      <p class="appointment-label">Your next Appointment</p>
      <div class="appointment-line"></div>
    </div>
    <div class="mascot-art" role="img" aria-label="Cartoon white poodle mascot illustration"></div>
    <p class="contact">27B Fenwick St Mudgee NSW 2850 Ph. 6319 5057</p>
  </section>
</main>
</body>
</html>
```